Dana's Pup Suds & Snip

I have a mobile dog grooming business and I need a design. I would like a scruffy dirty dog as a before dog. Then a clean short hair neatly groomed dog as the after been cleaned and groom by my service. Cartoon images would be good.
My services are bathing, drying, cleaning ears, clipping nails, clip and style hair and deodorising. The mobile van is white and my mobile number is 0461302857.
No dog in bath/tub designs please as they are too common.

Target Market(s)

Clients who wish their dogs to be clean and clipped, ready for the summer heat and Christmas where friends and family visit. They want their dog smelling nice and looking good.

Industry/Entity Type

Graphic Design

Contact Information for Business Card

DANA'S PUP SUDS & SNIP Mobile Grooming
Bath, Trim Nails, Clean Ears, Style Clip, Blow Dry,
Cologne. Call Us On: 0461302857

Font styles to use
Script

Colors
85cae6
34a6d7
0393ce
ec1f27

Requirements
Must have
• A Logo with a picture of 2 dogs.. One dirty dog, scruffy long hair, messy, neglected
• 2nd Dog, Clean, Hair neat Looking Sharp and well
• looked after.
• A comparison of two dogs the before and after shots of the same dog. Before it was groomed and after it was groomed. Cartoon form.
Nice to have
• The colour of my Van is White with a light blue stripe at the bottom. I would like colours to suit my trailer eg Grey's, Bubbles, or water drops. Red & Black writing.
• As I need business cards and vinyl sticker logo to put on my trailer.
Should not have
• No dogs in baths or tubs as they are too common in the Mobile Grooming Industry.
• Needs to be unique. .

```html
<!DOCTYPE html>
<html lang="en">
<head>
<meta charset="utf-8">
<title>Dana's Pup Suds &amp; Snip – Business Card</title>
<link rel="stylesheet" href="https://fonts.googleapis.com/css2?family=Open+Sans:wght@400;600;700&display=swap">
<style>
  :root {
    --white: #ffffff;
    --stage-grey: #a9a9ad;
    --brand-blue: #0393ce;
    --band-blue: #2a9fd8;
    --band-blue-light: #34a6d7;
    --band-edge: #85cae6;
    --tan: #c4996b;
    --call-red: #ec1f27;
    --ink: #2b2b2b;
    --dog-before: #b9a38c;
    --dog-after: #e4e4e6;
  }
  * { box-sizing: border-box; margin: 0; padding: 0; }
  html, body { width: 1200px; height: 863px; overflow: hidden; }
  body {
    font-family: "Open Sans", Arial, sans-serif;
    background: var(--white);
    position: relative;
  }
  .brand-header {
    position: absolute; left: 0; top: 0;
    width: 1200px; height: 280px;
    display: flex; align-items: center; justify-content: center; gap: 22px;
  }
  .brand-name {
    font-family: "Open Sans", Arial, sans-serif;
    font-weight: 600;
    font-size: 40px;
    color: var(--brand-blue);
    letter-spacing: 0.5px;
  }
  .dog-art {
    width: 76px; height: 76px;
    border-radius: 10px;
  }
  .dog-art--before { background: linear-gradient(160deg, var(--dog-before), #8a6d52); }
  .dog-art--after  { background: linear-gradient(160deg, var(--dog-after), #cfd3d8); }

  .stage {
    position: absolute; left: 0; top: 280px;
    width: 1200px; height: 583px;
    background: var(--stage-grey);
  }
  .business-card {
    position: absolute; left: 250px; top: 372px;
    width: 700px; height: 400px;
    background: var(--white);
    border-radius: 26px;
    overflow: hidden;
    box-shadow: 0 14px 30px rgba(0,0,0,0.25);
  }
  .card-logo {
    position: absolute; left: 0; top: 0;
    width: 700px; height: 190px;
    display: flex; align-items: center; justify-content: space-between;
    padding: 0 48px;
  }
  .card-logo .brand-name { font-size: 36px; }
  .card-logo .dog-art { width: 110px; height: 110px; }
  .service-band {
    position: absolute; left: 0; top: 200px;
    width: 700px; height: 110px;
    background: linear-gradient(180deg, var(--band-blue-light), var(--band-blue));
    border-top: 3px solid var(--band-edge);
    border-bottom: 3px solid var(--band-edge);
    color: var(--white);
    text-align: center;
    display: flex; flex-direction: column; justify-content: center; gap: 6px;
  }
  .service-title { font-weight: 700; font-size: 22px; }
  .service-list  { font-weight: 400; font-size: 19px; }
  .phone {
    position: absolute; left: 0; top: 324px;
    width: 700px;
    text-align: center;
    font-weight: 700;
    font-size: 34px;
    letter-spacing: 1px;
    color: var(--call-red);
  }
</style>
</head>
<body>
  <header class="brand-header">
    <div class="dog-art dog-art--before" role="img" aria-label="Cartoon of a scruffy, muddy dog before grooming"></div>
    <div class="brand-name">Dana's Pup Suds &amp; Snip</div>
    <div class="dog-art dog-art--after" role="img" aria-label="Cartoon of a clean, neatly groomed dog with a red bow and butterfly"></div>
  </header>

  <div class="stage"></div>

  <section class="business-card">
    <div class="card-logo">
      <div class="dog-art dog-art--before" role="img" aria-label="Cartoon of a scruffy, muddy dog before grooming"></div>
      <div class="brand-name">Dana's Pup Suds &amp; Snip</div>
      <div class="dog-art dog-art--after" role="img" aria-label="Cartoon of a clean, neatly groomed dog with a red bow and butterfly"></div>
    </div>
    <div class="service-band">
      <div class="service-title">Mobile Grooming</div>
      <div class="service-list">Bath, Trim Nails, Clean Ears, Style Clip, Blow Dry, Cologne</div>
    </div>
    <div class="phone">0461302857</div>
  </section>
</body>
</html>
```